The Gallowmere Notes Theatre Production Poster

We're after a poster for a theatre production based on R.T Ambrey's book, The Gallowmere Notes.
This play follows the story of a senior demon teaching a student demon how to tempt humankind. The tone of the play is light and formal with dark undertones and moments of levity. Hell is set in a university. I am wanting an eye-catching poster. Something subtle and NOT in the theme of 'horror'. I am open to different creative ideas, but I like the idea of a book being involved and maybe some shadow loosely representing a demon reading the book. Another idea could be a shadow hovering over a silhouetted human.
Other details that the poster must include:
- The Name of the Show: The Gallowmere Notes
- Time of the shows: 7:30 pm
- Dates of the show: Saturday 8th and 15th of October 2022
- Location: Brindlecombe Civic Theatre
- Organisation: Lanterngate Theatre Productions
- ticket price: $38
- bookings made at: https://app.seatvane-example.org.au/LanterngateTheatreProductions/Gallowmere
Target Market(s)
university Students
Industry/Entity Type
Theatre
Look and feel
Each slider illustrates characteristics of the customer's brand and the style your logo design should communicate.

```html
<!DOCTYPE html>
<html lang="en">
<head>
<meta charset="utf-8">
<title>The Gallowmere Notes – Poster</title>
<link rel="stylesheet" href="https://fonts.googleapis.com/css2?family=Yellowtail&family=Archivo+Black&family=Oswald:wght@600;700&family=Archivo:wght@800&display=swap">
<style>
  :root {
    --ink: #0b0b16;
    --band: #0a0a0c;
    --white: #ffffff;
    --lavender: #dcd8f4;
    --pink: #e7a6d2;
    --blush: #f3cde6;
    --sky: #c8c6ee;
    --blue: #4262c0;
    --deep-blue: #24358a;
    --ticket: #cfd2f1;
    --ticket-edge: #8e95cf;
    --ticket-navy: #1b2f55;
    --badge: #137487;
    --url-box: #1f4688;
  }
  * { box-sizing: border-box; margin: 0; padding: 0; }
  html, body { width: 927px; height: 1200px; overflow: hidden; background: var(--sky); }
  .poster { position: relative; width: 927px; height: 1200px; overflow: hidden; }

  .backdrop {
    position: absolute; inset: 0;
    background:
      radial-gradient(ellipse 55% 22% at 50% 8%, var(--blush), transparent 70%),
      radial-gradient(ellipse 45% 30% at 48% 52%, var(--deep-blue), transparent 70%),
      radial-gradient(ellipse 30% 25% at 8% 65%, var(--blue), transparent 75%),
      radial-gradient(ellipse 50% 18% at 50% 96%, var(--pink), transparent 75%),
      linear-gradient(180deg, var(--pink) 0%, var(--sky) 28%, #8d9de0 50%, var(--sky) 72%, var(--pink) 100%);
  }

  .title { position: absolute; left: 0; right: 0; text-align: center; }
  .title-the {
    top: 228px; font-family: "Yellowtail", cursive; font-size: 92px; line-height: 1;
    color: var(--white); text-shadow: 2px 3px 4px rgba(0,0,0,.35);
  }
  .title-main {
    top: 298px; font-family: "Yellowtail", cursive; font-size: 140px; line-height: 1;
    color: var(--lavender); padding-left: 40px;
    text-shadow: -3px -3px 0 var(--ink), 3px 4px 6px rgba(0,0,0,.45);
  }
  .title-sub {
    top: 428px; font-family: "Archivo Black", sans-serif; font-size: 54px; line-height: 1;
    letter-spacing: 6px; color: var(--ink); padding-right: 30px;
  }

  .scroll-band { position: absolute; }
  .scroll-band svg { position: absolute; inset: 0; width: 100%; height: 100%; }
  .scroll-band span { position: relative; display: block; text-align: center; color: var(--white); }

  .show-dates { left: 176px; top: 513px; width: 614px; height: 85px; }
  .show-dates span {
    font-family: "Oswald", sans-serif; font-weight: 700; font-size: 25px; line-height: 85px;
  }
  .show-dates small { font-size: 14px; font-weight: 600; }
  .show-dates sup { font-size: 11px; }

  .ticket { position: absolute; left: 244px; top: 662px; width: 492px; height: 197px; }
  .ticket svg { position: absolute; inset: 0; }
  .ticket-word {
    position: absolute; left: 106px; top: 40px; font-family: "Archivo Black", sans-serif;
    font-size: 38px; line-height: 1; color: var(--ticket-navy);
  }
  .ticket-price {
    position: absolute; left: 257px; top: 44px; width: 52px; height: 52px; border-radius: 50%;
    background: var(--badge); color: var(--white); font-family: "Oswald", sans-serif; font-weight: 700;
    font-size: 18px; line-height: 52px; text-align: center;
  }
  .ticket-show { position: absolute; left: 140px; top: 96px; width: 140px; text-align: center; color: var(--ticket-navy); line-height: 1; }
  .ticket-show .script { font-family: "Yellowtail", cursive; font-size: 23px; display: block; }
  .ticket-show .caps { font-family: "Archivo Black", sans-serif; font-size: 8px; letter-spacing: 1px; display: block; }
  .ticket-date {
    position: absolute; left: 62px; width: 240px; top: 134px; text-align: center;
    font-family: "Archivo", sans-serif; font-weight: 800; font-size: 6.5px; color: var(--ticket-navy);
  }
  .ticket-invite {
    position: absolute; left: 62px; top: 147px; width: 238px; height: 14px; background: var(--ticket-navy);
    color: var(--ticket); font-family: "Archivo", sans-serif; font-weight: 800; font-size: 9px;
    line-height: 14px; text-align: center; letter-spacing: .5px;
  }

  .venue-details {
    position: absolute; left: 0; right: 0; top: 893px; text-align: center;
    font-family: "Oswald", sans-serif; font-weight: 700; font-size: 31px; line-height: 49px; color: var(--ink);
  }

  .bookings-label { left: 321px; top: 1007px; width: 297px; height: 42px; }
  .bookings-label span { font-family: "Archivo", sans-serif; font-weight: 800; font-size: 19px; line-height: 42px; letter-spacing: .5px; }

  .booking-url {
    position: absolute; left: 32px; top: 1071px; width: 860px; height: 46px; border-radius: 10px;
    background: linear-gradient(180deg, #2f5fa6, var(--url-box) 55%, #17366e);
    border: 2px solid var(--white); box-shadow: 0 0 0 2px var(--ink);
    color: var(--white); font-family: "Archivo", sans-serif; font-weight: 800; font-size: 16.5px;
    line-height: 42px; text-align: center; white-space: nowrap;
  }
</style>
</head>
<body>
<main class="poster">
  <div class="backdrop" role="img" aria-label="Soft dreamy backdrop of pink and blue swirls, sparkles and drifting leaves"></div>

  <h1>
    <span class="title title-the">The</span>
    <span class="title title-main">Gallowmere</span>
    <span class="title title-sub">NOTES</span>
  </h1>

  <div class="scroll-band show-dates">
    <svg viewBox="0 0 614 85" preserveAspectRatio="none" aria-hidden="true">
      <rect x="4" y="14" width="606" height="57" fill="#0a0a0c"/>
      <rect x="4" y="4" width="4" height="77" fill="#0a0a0c"/>
      <rect x="606" y="4" width="4" height="77" fill="#0a0a0c"/>
      <circle cx="6" cy="5" r="5" fill="#0a0a0c"/><circle cx="6" cy="80" r="5" fill="#0a0a0c"/>
      <circle cx="608" cy="5" r="5" fill="#0a0a0c"/><circle cx="608" cy="80" r="5" fill="#0a0a0c"/>
    </svg>
    <span>7:30 PM &nbsp;|&nbsp; SATURDAY 18<sup>TH</sup> <small>AND</small> 15<sup>TH</sup> OF OCTOBER 2022</span>
  </div>

  <div class="ticket">
    <svg width="492" height="197" viewBox="0 0 492 197" aria-hidden="true">
      <path d="M4 4 H346 a12 12 0 0 0 24 0 H488 V193 H370 a12 12 0 0 0 -24 0 H4 Z" fill="#cfd2f1" stroke="#b3b8e4" stroke-width="2"/>
      <rect x="24" y="20" width="314" height="157" fill="none" stroke="#8e95cf" stroke-width="2"/>
      <rect x="31" y="27" width="300" height="143" fill="none" stroke="#4f5fa0" stroke-width="3" stroke-dasharray="0.1 8" stroke-linecap="round"/>
      <line x1="358" y1="22" x2="358" y2="176" stroke="#4f5fa0" stroke-width="2" stroke-dasharray="2 3"/>
      <rect x="382" y="20" width="86" height="157" fill="none" stroke="#8e95cf" stroke-width="2"/>
      <line x1="390" y1="28" x2="390" y2="170" stroke="#4f5fa0" stroke-width="3" stroke-dasharray="0.1 8" stroke-linecap="round"/>
      <line x1="460" y1="28" x2="460" y2="170" stroke="#4f5fa0" stroke-width="3" stroke-dasharray="0.1 8" stroke-linecap="round"/>
    </svg>
    <div class="ticket-word">TICKET</div>
    <div class="ticket-price">$38</div>
    <div class="ticket-show"><span class="script">Gallowmere</span><span class="caps">NOTES</span></div>
    <div class="ticket-date">7:30 PM | SATURDAY 18TH AND 15TH OF OCTOBER 2022</div>
    <div class="ticket-invite">YOU ARE INVITED</div>
  </div>

  <p class="venue-details">
    Location: Brindlecombe Civic Theatre<br>
    Organisation: Lanterngate Theatre Productions
  </p>

  <div class="scroll-band bookings-label">
    <svg viewBox="0 0 297 42" preserveAspectRatio="none" aria-hidden="true">
      <rect x="3" y="6" width="291" height="30" fill="#0a0a0c"/>
      <rect x="2" y="2" width="3" height="38" fill="#0a0a0c"/>
      <rect x="292" y="2" width="3" height="38" fill="#0a0a0c"/>
      <circle cx="3.5" cy="3" r="3" fill="#0a0a0c"/><circle cx="3.5" cy="39" r="3" fill="#0a0a0c"/>
      <circle cx="293.5" cy="3" r="3" fill="#0a0a0c"/><circle cx="293.5" cy="39" r="3" fill="#0a0a0c"/>
    </svg>
    <span>BOOKINGS MADE AT</span>
  </div>

  <div class="booking-url">https://app.seatvane-example.org.au/LanterngateTheatreProductions/Gallowmere</div>
</main>
</body>
</html>
```